Bully breed rescue website

I need a website for my bully breed rescue. We rescue bully breeds from up and down the east coast of the United States and train them as service dogs for people with limited mobility disabilities. I don't want a lot of white space. I want it to be modern and slick and colorful and still look professional. I want it to be different and have a lot of wow factor. I linked a copy of my logo.

Number of Pages Required

5+ page

Font styles to use
Sans Serif

Colors

Designer to choose colors to be used in the design.

Requirements
Must have
• Moving aspects. Blog and ecommerce.
• 1.) Home page
• 2.) Services- something modular
• 3.) About US
• 4.) Blog
• 5.) Application page
• 6.) Donation page
• 7.) Contact Us
Nice to have
• Large Slider of photos on home page
• vertical menu bar
Should not have
• Lots of white space. Dont want it to look like a template or any other site

```html
<!DOCTYPE html>
<html lang="en">
<head>
<meta charset="utf-8">
<title>Loyal Paws Rescue — Home</title>
<link rel="stylesheet" href="https://fonts.googleapis.com/css2?family=Almendra:wght@700&display=swap">
<style>
  :root {
    --sky: #4aa1ec;
    --sky-deep: #2f97dc;
    --panel: rgba(50, 78, 110, 0.9);
    --panel-edge: #7596bd;
    --ink: #0c0c10;
    --paper: #ffffff;
    --accent: #e8202a;
  }
  * { margin: 0; padding: 0; box-sizing: border-box; }
  html, body { width: 1200px; height: 675px; overflow: hidden; background: var(--sky); }
  .home {
    position: relative;
    width: 1200px;
    height: 675px;
    overflow: hidden;
    background: var(--sky);
    font-family: "Almendra", serif;
    font-weight: 700;
    text-transform: uppercase;
  }
  .backdrop { position: absolute; inset: 0; }
  .brand {
    position: absolute;
    left: 27px;
    top: 124px;
    width: 326px;
    text-align: center;
    white-space: nowrap;
    font-size: 29px;
    line-height: 1;
    color: var(--ink);
    letter-spacing: 0.5px;
  }
  .tagline-box {
    position: absolute;
    left: 445px;
    top: 261px;
    width: 311px;
    height: 175px;
    background: var(--panel);
    border: 1px solid var(--panel-edge);
    padding: 31px 0 0 61px;
  }
  .tagline {
    color: var(--paper);
    font-size: 25px;
    line-height: 38px;
    letter-spacing: 1px;
    white-space: nowrap;
  }
  .main-nav {
    position: absolute;
    left: 46px;
    top: 442px;
  }
  .main-nav ul { list-style: none; }
  .main-nav a {
    display: block;
    color: var(--ink);
    text-decoration: none;
    font-size: 20px;
    line-height: 30px;
    letter-spacing: 1px;
    white-space: nowrap;
  }
  .main-nav a.is-highlight { color: var(--accent); }
</style>
</head>
<body>
  <main class="home">
    <svg class="backdrop" width="1200" height="675" viewBox="0 0 1200 675">
      <defs>
        <radialGradient id="hero-tones" cx="0.6" cy="0.45" r="0.75" fx="0.62" fy="0.5">
          <stop offset="0" stop-color="#a8664f"/>
          <stop offset="0.3" stop-color="#85492f"/>
          <stop offset="0.6" stop-color="#5a2e1c"/>
          <stop offset="0.85" stop-color="#331a10"/>
          <stop offset="1" stop-color="#1a0c07"/>
        </radialGradient>
      </defs>
      <polygon class="backdrop-band" points="0,0 388,0 0,576" fill="#2f97dc"/>
      <polygon class="hero-photo" points="826,0 1200,0 1200,675 560,675" fill="url(#hero-tones)"
               role="img" aria-label="Close-up photo of a brown bully breed dog resting its head on the floor"/>
    </svg>

    <div class="brand">Loyal Paws Rescue</div>

    <div class="tagline-box">
      <p class="tagline">Across the<br>East Coast of<br>the States</p>
    </div>

    <nav class="main-nav">
      <ul>
        <li><a href="#services">Services</a></li>
        <li><a href="#about">About Us</a></li>
        <li><a href="#blog">Blog</a></li>
        <li><a href="#applications">Applications</a></li>
        <li><a href="#donations" class="is-highlight">Donations</a></li>
        <li><a href="#contact">Contact Us</a></li>
      </ul>
    </nav>
  </main>
</body>
</html>
```